Larkfield Clinic Marketing Flyer

We are a new medical practice in the community and need a flyer to send to other medical offices to inform of our services. We just completed our logo with PixelGuild and would like to incorporate that plus our marketing content into the flyer. Our medical practice has 2 divisions: (1)Mental Health/Psychiatry and (2) Migraine and Neurospasticity Management. Please see website for content and provider photos at www.LarkfieldCare.example

Target Market(s)

Other Healthcare Professionals in the Community

Industry/Entity Type

Medical

Requirements
Must have
• Photos of all 5 healthcare providers, phone number, address, logo

```html
<!DOCTYPE html>
<html lang="en">
<head>
<meta charset="utf-8">
<title>Larkfield Clinic Flyer</title>
<link rel="stylesheet" href="https://fonts.googleapis.com/css2?family=Yeseva+One&family=Nunito+Sans:wght@400;600;700;800&display=swap">
<style>
:root{
  --bg:#d9d9d9;
  --green:#8ab041;
  --green-dark:#46642a;
  --beige:#d7d1a9;
  --ink:#2b2b2b;
  --teal:#2aa39b;
  --white:#ffffff;
}
*{box-sizing:border-box;margin:0;padding:0}
html,body{width:1200px;height:2374px;overflow:hidden;background:var(--bg);font-family:"Nunito Sans",sans-serif;color:var(--ink)}
.flyer{position:absolute;left:50px;top:408px;width:1100px;height:1558px;background:var(--white);box-shadow:0 6px 18px rgba(0,0,0,.25);overflow:hidden}
.abs{position:absolute}
.logo-box{left:0;top:0;width:347px;height:233px;background:var(--white);display:flex;align-items:center;justify-content:center;text-align:center}
.logo-name{font-family:"Nunito Sans",sans-serif;font-weight:700;font-size:36px;line-height:42px;color:var(--teal);letter-spacing:2px}
.dark-block{left:347px;top:0;width:181px;height:233px;background:var(--green-dark)}
.hero-panel{left:0;top:233px;width:528px;height:347px;background:var(--green);padding:16px 0 0 41px;color:var(--white)}
.headline{font-family:"Yeseva One",serif;font-size:53px;line-height:73px;font-weight:400}
.rule{width:150px;height:6px;background:var(--white);margin:10px 0 20px}
.hero-sub{font-size:24px;line-height:29px}
.hero-photo{left:528px;top:0;width:572px;height:580px;background:linear-gradient(160deg,#f1f1ee 0%,#e3e1da 45%,#c9a24a 75%,#8f8f88 100%)}
.providers-band{left:0;top:580px;width:1100px;height:261px;background:var(--beige)}
.section-title{width:100%;text-align:center;font-family:"Yeseva One",serif;font-size:41px;color:var(--green-dark)}
.providers-title{left:0;top:594px}
.providers-text{left:100px;top:654px;width:900px;text-align:center;font-size:18.5px;line-height:23px}
.headshot{top:751px;width:192px;height:230px;background:linear-gradient(180deg,#4d6a78 0%,#2f4550 60%,#22323a 100%)}
.provider{top:996px;width:216px;text-align:center;font-size:22px;line-height:27px}
.provider b{display:block;color:var(--green);font-weight:800}
.migraine-band{left:0;top:1061px;width:1100px;height:181px;background:var(--green)}
.migraine-title{left:0;top:1076px;color:var(--green-dark)}
.migraine-text{left:70px;top:1149px;width:960px;text-align:center;font-size:19px;line-height:24px;color:var(--white)}
.doctor-photo{left:41px;top:1282px;width:192px;height:231px;background:linear-gradient(180deg,#8a5a32 0%,#b07a48 45%,#e7dcc4 100%)}
.doctor-name{left:256px;top:1284px;font-size:24px;font-weight:800;color:var(--green)}
.doctor-role{left:256px;top:1320px;font-size:22px;line-height:27px}
.service{left:256px;width:267px;height:32px;background:var(--green);color:var(--white);font-size:17px;font-weight:800;padding:4px 12px}
.contact-panel{left:543px;top:1242px;width:557px;height:316px;background:var(--green-dark);color:var(--white)}
.moved-title{left:0;top:18px;width:557px;text-align:center;font-family:"Yeseva One",serif;font-size:40px;color:var(--green)}
.moved-text{left:0;top:82px;width:557px;text-align:center;font-size:19px;line-height:25px}
.line-label{font-size:19px}
.phone{font-size:21px;font-weight:800;display:flex;align-items:center;gap:8px;margin-top:2px}
.divider{left:236px;top:160px;width:2px;height:60px;background:var(--white)}
.contact-line{left:31px;font-size:20px;display:flex;align-items:center;gap:12px}
svg{display:block}
</style>
</head>
<body>
<main class="flyer">
  <div class="abs logo-box">
    <span class="logo-name">LARKFIELD<br>CLINIC</span>
  </div>
  <div class="abs dark-block"></div>
  <section class="abs hero-panel">
    <h1 class="headline">Helping Bodies<br>Helping Minds<br>Helping You</h1>
    <div class="rule"></div>
    <p class="hero-sub">Mental Health and Psychiatry Services<br>Migraine and Neurospasticity Intervention</p>
  </section>
  <div class="abs hero-photo" role="img" aria-label="Photo of a smiling woman in a yellow top sitting on a sofa looking at her phone"></div>

  <div class="abs providers-band"></div>
  <h2 class="abs section-title providers-title">Meet Our Mental Health Providers</h2>
  <p class="abs providers-text">Bringing comprehensive evaluation, medication management and psychotherapy to the full spectrum of mental health disorders including minor, moderate and major depression, bipolar disorder, ADD/ADHD, anxiety, schizophrenia, stress or grief reactions, and others.</p>

  <div class="abs headshot" style="left:131px" role="img" aria-label="Portrait of provider Tom Harwell"></div>
  <div class="abs headshot" style="left:347px" role="img" aria-label="Portrait of provider Shelby Jarrow"></div>
  <div class="abs headshot" style="left:563px" role="img" aria-label="Portrait of provider Ross Linden"></div>
  <div class="abs headshot" style="left:780px" role="img" aria-label="Portrait of provider Joan Garrick"></div>

  <p class="abs provider" style="left:119px"><b>Tom Harwell,</b>PMHNP - BC</p>
  <p class="abs provider" style="left:335px"><b>Shelby Jarrow,</b>PMHNP - BC</p>
  <p class="abs provider" style="left:551px"><b>Ross Linden</b>PMHNP - BC</p>
  <p class="abs provider" style="left:768px"><b>Joan Garrick,</b>PMHNP-BC</p>

  <div class="abs migraine-band"></div>
  <h2 class="abs section-title migraine-title">Migraine and Neurospasticity Intervention</h2>
  <p class="abs migraine-text">Injections of botulinum neurotoxin are a widely used therapeutic form of treatment for both chronic migraines and patients with involuntary muscle contractions (neurospasticity). Injections may offer up to 3 months of relief and may be combined with other pharmaceutical interventions for maximum benefit.</p>

  <div class="abs doctor-photo" role="img" aria-label="Portrait of Dr. Brent Sayles in front of a stone fireplace"></div>
  <p class="abs doctor-name">Dr. Brent Sayles</p>
  <p class="abs doctor-role">A board certified family<br>practice physician</p>
  <p class="abs service" style="top:1404px">New Patient Evaluation</p>
  <p class="abs service" style="top:1444px">Insurance Pre-Authorization</p>
  <p class="abs service" style="top:1484px">Follow-Up Appointments</p>

  <section class="abs contact-panel">
    <h2 class="abs moved-title">We MOVED!</h2>
    <p class="abs moved-text">Find us now at 120 Willowmere Drive,<br>Suite A Larkfield, ID</p>
    <div class="abs" style="left:31px;top:160px">
      <p class="line-label">Mental Health</p>
      <p class="phone"><svg width="20" height="20" viewBox="0 0 24 24"><path fill="#8ab041" d="M6.6 10.8a15.1 15.1 0 0 0 6.6 6.6l2.2-2.2c.3-.3.7-.4 1-.2 1.1.4 2.3.6 3.6.6.6 0 1 .4 1 1V20c0 .6-.4 1-1 1A17 17 0 0 1 3 4c0-.6.4-1 1-1h3.5c.6 0 1 .4 1 1 0 1.3.2 2.5.6 3.6.1.3 0 .7-.2 1z"/></svg>(555)010-4006</p>
    </div>
    <div class="abs divider"></div>
    <div class="abs" style="left:250px;top:160px">
      <p class="line-label">Migraine and Neurospasticity</p>
      <p class="phone"><svg width="20" height="20" viewBox="0 0 24 24"><path fill="#8ab041" d="M6.6 10.8a15.1 15.1 0 0 0 6.6 6.6l2.2-2.2c.3-.3.7-.4 1-.2 1.1.4 2.3.6 3.6.6.6 0 1 .4 1 1V20c0 .6-.4 1-1 1A17 17 0 0 1 3 4c0-.6.4-1 1-1h3.5c.6 0 1 .4 1 1 0 1.3.2 2.5.6 3.6.1.3 0 .7-.2 1z"/></svg>(555) 010-4886</p>
    </div>
    <p class="abs contact-line" style="top:234px"><svg width="20" height="16" viewBox="0 0 20 16"><rect width="20" height="16" rx="2" fill="#8ab041"/><path d="M1 2l9 7 9-7" stroke="#46642a" stroke-width="2" fill="none"/></svg>support@LarkfieldCare.example</p>
    <p class="abs contact-line" style="top:272px"><svg width="20" height="20" viewBox="0 0 20 20"><circle cx="10" cy="10" r="9" fill="none" stroke="#8ab041" stroke-width="2"/><ellipse cx="10" cy="10" rx="4" ry="9" fill="none" stroke="#8ab041" stroke-width="1.5"/><path d="M1 10h18" stroke="#8ab041" stroke-width="1.5"/></svg>www.LarkfieldCare.example</p>
  </section>
</main>
</body>
</html>
```